Hadley & Partners, LLC Business Card 2016

We need a new business card design for a very important trade show coming up.

We are a compliance Consulting Firm. Our clients are stock brokerage firms and investment advisers.

I would like our logo on both sides of the card.

Info in the front of the card shold include:

Logo
First & Last Name
Title
Office #
Cell #
Email
Company Address (42 W. Calloway St., Suite 300 Pasadena, CA 91417

Back of the card should include the logo and url: www.hadleypartnersgroup.com

Target Market(s)

Stock Brokerage Firms and Investment Advisers

Industry/Entity Type

Financial Service

Contact Information for Business Card

Marcus J. Pellew
President
42 W. Calloway St., Suite 300
Pasadena, CA 91417
O 626.555.0147 ext. 204
C 818.555.0193
Email: marcus@hadleypartnersgroup.com
www.hadleypartnersgroup.com

Requirements
Nice to have
• The back of the card could be black with the logo with the white letters.
• I do want the front of the card to at least have the color logo with the black "Hadley & Partners Lettering.

```html
<!DOCTYPE html>
<html lang="en">
<head>
<meta charset="utf-8">
<title>Hadley &amp; Partners — Business Card</title>
<link rel="stylesheet" href="https://fonts.googleapis.com/css2?family=Cinzel:wght@400&family=Roboto:wght@400;500&display=swap">
<style>
  :root {
    --stage: #5a4630;
    --card-light: #f2f2f2;
    --card-light-edge: #d6d6d6;
    --card-dark: #121212;
    --red: #c8201e;
    --ink: #2b2b2b;
    --white: #ffffff;
  }
  * { box-sizing: border-box; margin: 0; padding: 0; }
  html, body { width: 1200px; height: 1023px; overflow: hidden; }
  body {
    background: var(--stage);
    font-family: "Roboto", sans-serif;
    position: relative;
  }
  .card {
    position: absolute;
    top: 345px;
    width: 540px;
    height: 309px;
    border-radius: 16px;
    box-shadow: 0 12px 30px rgba(0,0,0,.45);
    overflow: hidden;
  }
  .card--front {
    left: 40px;
    background: radial-gradient(ellipse at 60% 40%, #fbfbfb, var(--card-light) 55%, var(--card-light-edge));
  }
  .card--back { left: 620px; background: var(--card-dark); }

  /* brand lockup */
  .brand {
    position: absolute; left: 34px; top: 44px;
    display: flex; align-items: center; gap: 14px;
    font-family: "Cinzel", serif; font-weight: 400; color: var(--ink);
  }
  .brand__mark { width: 34px; height: 34px; background: var(--red); flex: none; }
  .brand__name { font-size: 34px; line-height: 1; letter-spacing: 1px; white-space: nowrap; }
  .brand__sub { display: block; font-size: 13px; letter-spacing: 7px; margin-top: 4px; }

  /* front */
  .divider {
    position: absolute; left: 0; top: 172px; width: 442px; height: 1px; background: var(--red);
  }
  .divider::after {
    content: ""; position: absolute; left: 442px; top: -34px; width: 80px; height: 1px; background: var(--red);
  }
  .divider__step {
    position: absolute; left: 442px; top: 138px; width: 1px; height: 35px; background: var(--red);
  }
  .person { position: absolute; right: 18px; top: 104px; text-align: right; }
  .person__name { font-size: 25px; font-weight: 500; color: var(--ink); letter-spacing: .5px; }
  .person__title { font-size: 13px; color: var(--red); margin-top: 6px; letter-spacing: .5px; }

  .contact { position: absolute; left: 34px; bottom: 26px; list-style: none; }
  .contact li {
    display: flex; align-items: center; gap: 10px;
    font-size: 13px; color: var(--ink); line-height: 21px; letter-spacing: .3px;
  }
  .contact .icon {
    width: 15px; height: 15px; border-radius: 50%; background: var(--red);
    display: inline-flex; align-items: center; justify-content: center; flex: none;
  }

  .address {
    position: absolute; right: 22px; top: 192px; text-align: right; font-style: normal;
    font-size: 14px; line-height: 20px; color: var(--red); letter-spacing: .3px;
  }

  /* back */
  .band {
    position: absolute; left: 0; right: 0; top: 34px; height: 26px; background: var(--red);
    display: flex; align-items: center; justify-content: center;
    color: var(--white); font-size: 13px; letter-spacing: 1.5px;
  }
  .brand--back {
    left: 50%; top: 140px; transform: translateX(-50%); color: var(--white); gap: 18px;
  }
  .brand--back .brand__mark { width: 44px; height: 44px; }
  .brand--back .brand__name { font-size: 40px; }
  .brand--back .brand__sub { font-size: 15px; letter-spacing: 9px; }
</style>
</head>
<body>
  <section class="card card--front" aria-label="Business card front">
    <div class="brand">
      <span class="brand__mark"></span>
      <div class="brand__name">HADLEY<span class="brand__sub">&amp; PARTNERS</span></div>
    </div>

    <div class="divider"></div>
    <div class="divider__step"></div>

    <div class="person">
      <p class="person__name">Marcus J. Pellew</p>
      <p class="person__title">President</p>
    </div>

    <ul class="contact">
      <li><span class="icon"><svg width="9" height="9" viewBox="0 0 10 10"><path d="M2 1l2 2-1 1.2c.6 1.2 1.6 2.2 2.8 2.8L7 6l2 2-1.2 1.4C4.5 9 1 5.5.6 2.2z" fill="#fff"/></svg></span>626.555.0147 ext. 204</li>
      <li><span class="icon"><svg width="8" height="9" viewBox="0 0 8 10"><rect x="1" y=".5" width="6" height="9" rx="1" fill="none" stroke="#fff"/></svg></span>818.555.0193</li>
      <li><span class="icon"><svg width="9" height="7" viewBox="0 0 10 8"><rect x=".5" y=".5" width="9" height="7" fill="none" stroke="#fff"/><path d="M.5 .5L5 4.5 9.5 .5" fill="none" stroke="#fff"/></svg></span>marcus@hadleypartnersgroup.com</li>
    </ul>

    <address class="address">
      42 W. Calloway St., Suite 300<br>Pasadena, CA 91417
    </address>
  </section>

  <section class="card card--back" aria-label="Business card back">
    <div class="band">www.hadleypartnersgroup.com</div>
    <div class="brand brand--back">
      <span class="brand__mark"></span>
      <div class="brand__name">HADLEY<span class="brand__sub">&amp; PARTNERS</span></div>
    </div>
  </section>
</body>
</html>
```